BRELLANDA EXTRA VIRGIN OLIVE OIL

I needs a design for an Australian Extra Virgin Olive Oil.

The label will go on a round clear bottle

The label size front and back is 145mm high x 60mm wide.

The important points for the design are as follows.

I want to see elegant olives on the label so that non English speaking markets can easily understand its olive oil. I want it too look classy . IT must also look Australian but I don't want to see kangaroos just colours that reflect Australia.

The mandatory info on front label will be

BRELLANDA

Cold Pressed
EXTRA VIRGIN OLIVE OIL

AUSTRALIAN

1 litre

```html
<!DOCTYPE html>
<html lang="en">
<head>
<meta charset="utf-8">
<title>Brellanda Extra Virgin Olive Oil – Front Label</title>
<link rel="stylesheet" href="https://fonts.googleapis.com/css2?family=Marcellus&family=Marcellus+SC&display=swap">
<style>
  :root {
    --page-bg: #ffffff;
    --label-black: #060606;
    --wattle-gold: #ffcb2e;
    --gum-green: #1e9a55;
    --divider-green: #1f6b3d;
    --text-white: #f4f4f4;
    --olive-light: #c9dc4a;
    --olive-mid: #8fb52b;
    --olive-deep: #3f6d1f;
  }
  html, body {
    margin: 0;
    padding: 0;
    width: 1080px;
    height: 1200px;
    overflow: hidden;
    background: var(--page-bg);
  }
  .canvas {
    position: relative;
    width: 1080px;
    height: 1200px;
  }
  .front-label {
    position: absolute;
    left: 316px;
    top: 64px;
    width: 448px;
    height: 1072px;
  }
  .label-border { fill: var(--wattle-gold); stroke: var(--wattle-gold); stroke-width: 20; stroke-linejoin: round; }
  .label-body { fill: var(--label-black); stroke: var(--label-black); stroke-width: 14; stroke-linejoin: round; }
  .label-stitch { fill: none; stroke: var(--wattle-gold); stroke-width: 0.8; stroke-dasharray: 2 2; stroke-linejoin: round; }
  .name-band { fill: var(--wattle-gold); }
  .name-band-tab { fill: var(--gum-green); }
  .brand-name { font-family: "Marcellus SC", "Marcellus", serif; font-size: 22px; fill: var(--label-black); letter-spacing: 0.5px; }
  .process-line { font-family: "Marcellus", serif; font-size: 18px; fill: var(--wattle-gold); letter-spacing: 0.5px; }
  .product-line { font-family: "Marcellus", serif; font-size: 33px; fill: var(--text-white); letter-spacing: 0.5px; }
  .origin-line { font-family: "Marcellus", serif; font-size: 15px; fill: var(--wattle-gold); letter-spacing: 0.5px; }
  .volume-line { font-family: "Marcellus SC", serif; font-size: 14px; fill: var(--text-white); }
  .divider { stroke: var(--divider-green); stroke-width: 1; }
</style>
</head>
<body>
<main class="canvas">
  <svg class="front-label" viewBox="0 0 280 670" xmlns="http://www.w3.org/2000/svg">
    <defs>
      <clipPath id="label-interior">
        <polygon points="70,12 210,12 266,331 218,658 62,658 14,331"/>
      </clipPath>
      <radialGradient id="olive-tones" cx="40%" cy="45%" r="60%">
        <stop offset="0%" stop-color="var(--olive-light)"/>
        <stop offset="60%" stop-color="var(--olive-mid)"/>
        <stop offset="100%" stop-color="var(--olive-deep)" stop-opacity="0"/>
      </radialGradient>
    </defs>

    <polygon class="label-border" points="68,10 212,10 270,331 220,660 60,660 10,331"/>
    <polygon class="label-body" points="72,22 208,22 258,331 212,648 68,648 22,331"/>
    <polygon class="label-stitch" points="76,28 204,28 252,331 208,642 72,642 28,331"/>

    <g class="name-band-group" clip-path="url(#label-interior)">
      <path class="name-band" d="M0,82 Q140,66 280,82 L280,120 Q140,106 0,120 Z"/>
      <rect class="name-band-tab" x="40" y="74" width="14" height="50"/>
      <rect class="name-band-tab" x="226" y="74" width="14" height="50"/>
    </g>
    <text class="brand-name" x="140" y="103" text-anchor="middle">BRELLANDA</text>

    <text class="process-line" x="140" y="163" text-anchor="middle">COLD</text>
    <text class="process-line" x="140" y="189" text-anchor="middle">PRESSED</text>

    <line class="divider" x1="56" y1="225" x2="224" y2="225"/>

    <text class="product-line" x="140" y="274" text-anchor="middle">EXTRA</text>
    <text class="product-line" x="140" y="322" text-anchor="middle">VIRGIN</text>
    <text class="product-line" x="140" y="370" text-anchor="middle">OLIVE OIL</text>

    <line class="divider" x1="56" y1="390" x2="224" y2="390"/>

    <rect class="olive-illustration" role="img" aria-label="Illustration of two green olives on a leafy olive branch"
          x="62" y="405" width="150" height="140" rx="40" fill="url(#olive-tones)"/>

    <text class="origin-line" x="140" y="585" text-anchor="middle">AUSTRALIAN</text>
    <text class="volume-line" x="140" y="627" text-anchor="middle">1 litre</text>
  </svg>
</main>
</body>
</html>
```